Verdant Nest Interiors & Design
offering design and staging services for the homeowner
Simple
Maren Tolley
President
4517 North Willow Court
Centennial, CO 80122
info@verdantnestinteriorsdesign.example
Bright green color shown on the logo should be the entire back of the business card
logo file .ai

```html
<!DOCTYPE html>
<html lang="en">
<head>
<meta charset="utf-8">
<title>Verdant Nest Interiors &amp; Design — Stationery</title>
<link href="https://fonts.googleapis.com/css2?family=Questrial&display=swap" rel="stylesheet">
<style>
  :root{
    --green:#a9c93b;
    --ink:#4a4a4a;
    --muted:#9a9a9a;
    --rule:#cfcfcf;
    --paper:#ffffff;
    --stage:#e9e7e3;
    --faint:#eef3dc;
  }
  *{box-sizing:border-box;margin:0;padding:0}
  html,body{width:1200px;height:444px;overflow:hidden}
  body{background:var(--stage);font-family:"Questrial",Arial,sans-serif;color:var(--ink);position:relative}
  .sheet{position:absolute;background:var(--paper);box-shadow:0 2px 6px rgba(0,0,0,.18)}
  .letterhead{top:43px;width:196px;height:330px}
  .lh-1{left:19px}.lh-2{left:298px}.lh-3{left:571px}
  .brand{color:var(--green);font-size:9.5px;letter-spacing:.2px;white-space:nowrap}
  .letterhead .brand{position:absolute;top:16px;left:0;right:0;text-align:center}
  .lh-2 .brand{top:14px;left:14px;right:auto;text-align:left;line-height:1.15;white-space:normal;width:70px}
  .faint-name{position:absolute;left:14px;bottom:80px;color:var(--faint);font-size:20px;line-height:1.1;width:170px}
  .footer{position:absolute;left:12px;right:12px;bottom:12px;border-top:1px solid var(--green);padding-top:4px;font-size:3.6px;color:var(--muted);white-space:nowrap;text-align:center}
  .contact-block{position:absolute;top:14px;right:12px;width:80px;font-size:3.8px;line-height:1.5;color:var(--muted);text-align:left;border-left:1px solid var(--green);padding-left:4px;white-space:nowrap}
  .fax-title{position:absolute;top:44px;left:14px;font-size:15px;color:var(--ink);letter-spacing:.5px}
  .fax-fields{position:absolute;top:70px;left:14px;right:14px;display:grid;grid-template-columns:1fr 1fr;column-gap:10px;row-gap:9px}
  .field{font-size:4.5px;color:var(--ink);border-bottom:1px solid var(--rule);padding-bottom:2px}
  .fax-checks{position:absolute;top:128px;left:14px;right:14px;display:flex;justify-content:space-between;font-size:3.8px;color:var(--ink)}
  .check::before{content:"";display:inline-block;width:4px;height:4px;border:.6px solid var(--ink);margin-right:2px;vertical-align:-1px}
  .fax-rule{position:absolute;top:140px;left:14px;right:14px;border-top:1px solid var(--ink)}
  .option-label{position:absolute;top:380px;width:196px;text-align:center;font-size:12px;color:#333}
  .envelope{position:absolute;box-shadow:0 2px 5px rgba(0,0,0,.15)}
  .env-back{left:828px;top:142px;width:360px;height:112px}
  .env-front{left:859px;top:29px;width:329px;height:105px}
  .card{position:absolute;top:312px;height:60px;box-shadow:0 2px 5px rgba(0,0,0,.2)}
  .card-front{left:936px;width:84px;background:var(--paper)}
  .card-front .brand{position:absolute;top:8px;left:6px;font-size:5px}
  .card-front .details{position:absolute;left:6px;bottom:6px;font-size:2.8px;line-height:1.5;color:var(--muted)}
  .card-back{left:1039px;width:137px;background:var(--green);display:flex;align-items:center;justify-content:center}
  .card-back .brand{color:#fff;font-size:7.5px}
</style>
</head>
<body>

<section class="sheet letterhead lh-1" aria-label="Letterhead option 1">
  <div class="brand">verdant nest interiors &amp; design</div>
  <div class="faint-name">verdant nest interiors &amp; design</div>
  <div class="footer">4517 North Willow Court · Centennial, CO 80122 · (303) 555-0148 · info@verdantnestinteriorsdesign.example</div>
</section>
<div class="option-label" style="left:19px">Option-1</div>

<section class="sheet letterhead lh-2" aria-label="Letterhead option 2">
  <div class="brand">verdant nest<br>interiors &amp; design</div>
  <div class="contact-block">Maren Tolley, President<br>4517 North Willow Court<br>Centennial, CO 80122<br>(303) 555-0148<br>info@verdantnestinteriorsdesign.example</div>
  <div class="faint-name">verdant nest interiors &amp; design</div>
  <div class="footer">4517 North Willow Court · Centennial, CO 80122 · info@verdantnestinteriorsdesign.example</div>
</section>
<div class="option-label" style="left:298px">Option-2</div>

<section class="sheet letterhead lh-3" aria-label="Fax cover sheet option 3">
  <div class="fax-title">FAX</div>
  <div class="fax-fields">
    <div class="field">To:</div><div class="field">From:</div>
    <div class="field">Fax:</div><div class="field">Pages:</div>
    <div class="field">Phone:</div><div class="field">Date:</div>
    <div class="field">Re:</div><div class="field">CC:</div>
  </div>
  <div class="fax-checks">
    <span class="check">Urgent</span><span class="check">For Review</span><span class="check">Please Comment</span><span class="check">Please Reply</span><span class="check">Please Recycle</span>
  </div>
  <div class="fax-rule"></div>
  <div class="footer">4517 North Willow Court · Centennial, CO 80122 · (303) 555-0148 · info@verdantnestinteriorsdesign.example</div>
</section>
<div class="option-label" style="left:571px">Option-3</div>

<svg class="envelope env-back" viewBox="0 0 360 112" aria-label="Envelope back">
  <rect x="0" y="0" width="360" height="112" fill="#fff"/>
  <path d="M0 0 Q180 64 360 0" fill="none" stroke="#d6d6d6" stroke-width="1"/>
  <text x="18" y="98" font-family="Questrial, Arial, sans-serif" font-size="6" fill="#a9c93b">verdant nest interiors &amp; design</text>
</svg>

<svg class="envelope env-front" viewBox="0 0 329 105" aria-label="Envelope with green flap">
  <rect x="0" y="0" width="329" height="105" fill="#fff"/>
  <path d="M0 0 H329 V18 Q164.5 72 0 18 Z" fill="#a9c93b"/>
  <text x="164.5" y="24" text-anchor="middle" font-family="Questrial, Arial, sans-serif" font-size="11" fill="#ffffff">verdant nest interiors &amp; design</text>
  <text x="18" y="92" font-family="Questrial, Arial, sans-serif" font-size="5" fill="#9a9a9a">4517 North Willow Court · Centennial, CO 80122</text>
</svg>

<section class="card card-front" aria-label="Business card front">
  <div class="brand">verdant nest interiors &amp; design</div>
  <div class="details">Maren Tolley · President<br>4517 North Willow Court, Centennial, CO 80122<br>info@verdantnestinteriorsdesign.example</div>
</section>
<section class="card card-back" aria-label="Business card back">
  <div class="brand">verdant nest interiors &amp; design</div>
</section>

</body>
</html>
```